BRL business card

For a business card with our logo

Contact Information for Business Card

Mathéo VRANEL
Founder & CEO
email : ceo@brightlanterncollective.com / www.brightlanterncollective.com /
instagram / facebook / WhatsApp
N°: +590 690 482 517

Colors

Designer to choose colors to be used in the design.

```html
<!DOCTYPE html>
<html lang="en">
<head>
<meta charset="utf-8">
<title>BRL business card</title>
<link rel="stylesheet" href="https://fonts.googleapis.com/css2?family=Poppins:wght@400;500;600&display=swap">
<style>
  :root {
    --backdrop: #1d1d1d;
    --card-back: #1a1a1a;
    --card-front: #2a2a2b;
    --orange: #f26b21;
    --blue: #1f5ea8;
    --white: #f2f2f2;
    --grey: #6e6e6e;
    --grey-soft: #3a3a3a;
    --faint-mark: #3a2c25;
  }
  * { margin: 0; padding: 0; box-sizing: border-box; }
  html, body {
    width: 1200px; height: 882px; overflow: hidden;
    background: var(--backdrop);
    font-family: "Poppins", sans-serif;
  }
  .canvas { position: relative; width: 1200px; height: 882px; }

  .card {
    position: absolute; width: 560px; height: 320px;
    overflow: hidden;
  }
  .card--back { left: 60px; top: 100px; background: var(--card-back); }
  .card--front { left: 580px; top: 462px; background: var(--card-front); }

  /* back side */
  .back-brand {
    position: absolute; left: 0; right: 0; top: 112px;
    display: flex; align-items: center; justify-content: center; gap: 16px;
  }
  .back-brand__dot {
    width: 46px; height: 46px; border-radius: 50%;
    background: var(--grey-soft);
  }
  .back-brand__name {
    font-size: 30px; font-weight: 600; letter-spacing: 3px;
    color: var(--grey);
  }
  .social-row {
    position: absolute; right: 150px; top: 200px;
    display: flex; gap: 14px;
  }
  .social-row__item {
    width: 26px; height: 26px; border-radius: 50%;
    background: var(--grey-soft);
  }

  /* front side */
  .faint-mark {
    position: absolute; right: -40px; top: 40px;
    width: 330px; height: 330px; border-radius: 50%;
    background: var(--faint-mark); opacity: .55;
  }
  .front-brand {
    position: absolute; left: 40px; top: 52px;
    display: flex; flex-direction: column; align-items: flex-start; gap: 12px;
  }
  .front-brand__dot {
    width: 78px; height: 78px; border-radius: 50%;
    background: var(--orange); margin-left: 50px;
  }
  .front-brand__name {
    font-size: 19px; font-weight: 600; letter-spacing: 1.5px;
    color: var(--blue); line-height: 1.2;
  }
  .person {
    position: absolute; right: 40px; top: 110px; text-align: right;
  }
  .person__name { font-size: 26px; font-weight: 600; color: var(--orange); }
  .person__role { font-size: 16px; font-weight: 400; color: var(--white); margin-top: 2px; }

  .contact {
    position: absolute; left: 40px; bottom: 34px;
    list-style: none; display: flex; flex-direction: column; gap: 8px;
  }
  .contact__item {
    display: flex; align-items: center; gap: 12px;
    font-size: 15px; color: var(--white);
  }
  .contact__icon { width: 16px; height: 16px; flex: none; }
  .contact__accent { color: var(--orange); }
</style>
</head>
<body>
<main class="canvas">

  <section class="card card--back" aria-label="Card back">
    <div class="back-brand">
      <span class="back-brand__dot"></span>
      <span class="back-brand__name">BRIGHT LANTERN</span>
    </div>
    <div class="social-row" aria-label="Social profiles">
      <span class="social-row__item" role="img" aria-label="Social profile icon"></span>
      <span class="social-row__item" role="img" aria-label="Social profile icon"></span>
      <span class="social-row__item" role="img" aria-label="Messaging icon"></span>
    </div>
  </section>

  <section class="card card--front" aria-label="Card front">
    <div class="faint-mark"></div>

    <div class="front-brand">
      <span class="front-brand__dot"></span>
      <span class="front-brand__name">BRIGHT LANTERN<br>COLLECTIVE</span>
    </div>

    <div class="person">
      <p class="person__name">Mathéo VRANEL</p>
      <p class="person__role">Founder &amp; CEO</p>
    </div>

    <ul class="contact">
      <li class="contact__item">
        <svg class="contact__icon" viewBox="0 0 16 16"><path fill="#f26b21" d="M3.5 1.5l2.5 3-1.5 1.5c.8 2 2.5 3.7 4.5 4.5l1.5-1.5 3 2.5-1.5 2.5C7 14 2 9 1 3z"/></svg>
        +590 690 482 517
      </li>
      <li class="contact__item">
        <svg class="contact__icon" viewBox="0 0 16 16"><rect x="1" y="3" width="14" height="10" fill="#f26b21"/><path d="M1 3l7 6 7-6" fill="none" stroke="#2a2a2b" stroke-width="1.4"/></svg>
        ceo@brightlanterncollective.com
      </li>
      <li class="contact__item">
        <svg class="contact__icon" viewBox="0 0 16 16"><circle cx="8" cy="8" r="7" fill="#f26b21"/><path d="M1 8h14M8 1c-3 3.5-3 10.5 0 14M8 1c3 3.5 3 10.5 0 14" fill="none" stroke="#2a2a2b" stroke-width="1"/></svg>
        <span>www.<span class="contact__accent">brightlanterncollective</span>.com</span>
      </li>
    </ul>
  </section>

</main>
</body>
</html>
```